Corporate Web Redesign Project - coded

We would like redesign/refresh of our current site that would allow us to increase the depth of content and create a high quality impression for visitors.

Current site - http://corvanisystems.example/

A previous web redesign project has improved our site but it has not really reached the level we require.

Our customers are global, blue chip, organisations and a professional, corporate style of site is required.

Please note we would prefer a coded website to a just a design. We are happy to provide a zip of our current site if required.
Updates

                                   

Target Market(s)

Global oil and gas producers, KT, Pardo, Valmira etc.

Industry/Entity Type

It Professional

Requirements
Must have
• Design should support the level of content we currently have in the existing sitemap - although it should be expandable a site design for a large / complex site would not be appropriate

All current content / pages to be reflected in design

Must be visually appealing

Intuitive and clear navigation that is expandable

Display a high level of professionalism

Use a consistent palette of colours that complements our logo

Clean and organized layout

A way to capture visitor’s information or Call to action (i.e. contact link or form) on every page

Prominent Contact Information
Should not have
• Flash

```html
<!DOCTYPE html>
<html lang="en">
<head>
<meta charset="utf-8">
<title>Corvani Systems – The Business of Drilling Wells</title>
<link rel="stylesheet" href="https://fonts.googleapis.com/css2?family=Open+Sans:wght@400;600;700&family=Roboto+Condensed:wght@400;700&display=swap">
<style>
:root{
  --teal:#245869;
  --teal-dark:#1d4a59;
  --teal-text:#1f4f60;
  --olive:#7d8a55;
  --green:#55701f;
  --ink:#333;
  --muted:#555;
  --panel:#e6e6e6;
  --band:#f3f3f3;
  --white:#fff;
  --line:#dcdcdc;
}
*{box-sizing:border-box;margin:0;padding:0}
html,body{width:892px;height:1200px;overflow:hidden}
body{position:relative;background:var(--white);font-family:"Open Sans",Arial,sans-serif;color:var(--ink)}
.abs{position:absolute}

/* header */
.site-header{left:0;top:0;width:892px;height:70px;border-bottom:4px solid var(--teal)}
.brand{left:97px;top:14px;display:flex;align-items:center;gap:8px;font-weight:700;font-size:17px;color:var(--teal)}
.brand-dot{width:28px;height:28px;border-radius:50%;background:var(--teal)}
.info-call{right:97px;top:8px;font-size:12.5px;color:#8a8a8a}
.info-call strong{color:var(--green);font-weight:600}
.main-nav{right:97px;top:39px;display:flex}
.main-nav a{display:block;height:27px;line-height:28px;padding:0 20px;font-size:10.5px;font-weight:600;color:#333;text-decoration:none;text-transform:uppercase}
.main-nav a.active{background:var(--teal);color:var(--white);border-radius:3px 3px 0 0}

/* hero */
.hero{left:0;top:70px;width:892px;height:326px;background:linear-gradient(180deg,#74c8e6 0%,#a9dcef 55%,#dfeef2 80%,#c9d6dc 100%)}
.hero-photo{left:440px;top:70px;width:452px;height:326px;background:radial-gradient(ellipse at 40% 55%,#c85a4e 0%,#a9766a 22%,rgba(170,200,215,.5) 55%,rgba(0,0,0,0) 75%)}
.hero-copy{left:115px;top:115px;color:var(--teal-text);font-family:"Roboto Condensed",Arial,sans-serif}
.hero-kicker{font-size:20px;font-weight:700;line-height:24px}
.hero-title{font-size:40px;font-weight:700;line-height:44px;margin-bottom:14px}
.hero-points{list-style:none}
.hero-points li{position:relative;padding-left:20px;font-size:17px;line-height:20px;margin-bottom:8px}
.hero-points svg{position:absolute;left:0;top:3px}

/* services */
.services{left:97px;top:412px;width:467px;height:220px}
.service{position:absolute;width:233px;height:110px}
.service.s1{left:0;top:0}.service.s2{left:234px;top:0;border-left:1px solid var(--line)}
.service.s3{left:0;top:111px;border-top:1px solid var(--line)}.service.s4{left:234px;top:111px;border-top:1px solid var(--line);border-left:1px solid var(--line)}
.service-icon{position:absolute;left:1px;top:4px;width:68px;height:68px;border-radius:50%;background:var(--olive);display:flex;align-items:center;justify-content:center}
.s2 .service-icon,.s4 .service-icon{left:12px}
.service-body{position:absolute;left:78px;top:0;width:155px}
.s2 .service-body,.s4 .service-body{left:88px;width:148px}
.s3 .service-body,.s3 .service-icon,.s4 .service-body,.s4 .service-icon{margin-top:12px}
.service h3{font-size:12.5px;font-weight:600;color:var(--green);margin-bottom:6px;white-space:nowrap;letter-spacing:-.1px}
.service p{font-size:9px;line-height:14px;color:var(--ink)}
.read-more{display:inline-block;margin-top:9px;height:16px;line-height:14px;padding:0 8px;border:1px solid #bbb;border-radius:8px;font-size:8.5px;color:#555;background:linear-gradient(#fff,#ececec)}
.read-more b{font-weight:700;margin-left:3px}

/* welcome */
.welcome{left:97px;top:666px;width:467px}
.welcome h2{font-size:17px;font-weight:400;color:#555;margin-bottom:12px}
.welcome h2 strong{color:var(--teal-text);font-weight:600}
.welcome p{font-size:10.2px;line-height:16px;color:#333;margin-bottom:16px;letter-spacing:-.1px}

/* news */
.news{left:585px;top:416px;width:209px;height:389px;background:var(--panel)}
.news-head{height:42px;background:var(--teal);color:var(--white);font-size:16px;font-weight:600;line-height:42px;padding-left:14px}
.news-list{list-style:none;padding:8px 14px 0}
.news-item{display:flex;gap:8px;padding:8px 0 10px;border-bottom:1px solid #fff}
.news-item:last-child{border-bottom:0}
.news-logo{flex:0 0 43px;height:43px;background:var(--white);border:2px solid #cfcfcf;font-size:7px;font-weight:700;color:var(--teal);display:flex;align-items:center;justify-content:center;text-align:center;line-height:8px}
.news-item h4{font-size:8.5px;font-weight:700;color:#111;line-height:12px}
.news-item p{font-size:8.5px;line-height:12px;color:#555;margin-top:2px}

/* clients */
.clients{left:0;top:834px;width:892px;height:100px;background:var(--band)}
.client{position:absolute;top:11px;width:83px;height:76px;background:var(--white);border:2px solid #ddd;display:flex;align-items:center;justify-content:center;font-size:11px;font-weight:600;color:#3c5a66}

/* footer */
.site-footer{left:0;top:934px;width:892px;height:221px;background:var(--teal);color:var(--white)}
.footer-title{font-size:13px;font-weight:600}
.region{font-size:11.5px;font-weight:600;margin-bottom:12px}
.contact-line{position:relative;padding-left:18px;font-size:9px;line-height:13px;margin-bottom:8px}
.contact-line svg{position:absolute;left:0;top:1px}
.footer-divider{left:444px;top:0;width:1px;height:221px;background:#3c6f7f}
.field{position:absolute;height:22px;background:var(--white);border:1px solid #c8d2d6;border-radius:3px;font-size:9.5px;color:#333;padding:4px 6px}
.submit{left:457px;top:180px;width:75px;height:27px;border-radius:4px;background:linear-gradient(#fff,#c9c9c9);color:#222;font-size:13px;font-weight:700;text-align:center;line-height:27px}

/* bottom bar */
.copyright{left:98px;top:1164px;font-size:9.5px;line-height:13px;color:#333}
.partner-badge{left:668px;top:1164px;width:126px;height:24px;background:var(--teal);border-radius:2px}
</style>
</head>
<body>

<header class="abs site-header">
  <div class="abs brand"><span class="brand-dot"></span>Corvani Systems</div>
  <div class="abs info-call">Information Call - <strong>44(0)1632 960418, (555)014 2290</strong></div>
  <nav class="abs main-nav">
    <a class="active" href="#">Home</a><a href="#">News</a><a href="#">About Us</a><a href="#">Solutions</a><a href="#">Contact Us</a>
  </nav>
</header>

<section class="abs hero" role="img" aria-label="Photograph of oil pump jacks on a snowy field under a blue sky"></section>
<div class="abs hero-photo" role="img" aria-label="Red oil pump jack and drilling rig structure"></div>
<div class="abs hero-copy">
  <div class="hero-kicker">THE BUSINESS OF</div>
  <div class="hero-title">DRILLING WELLS</div>
  <ul class="hero-points">
    <li><svg width="11" height="14" viewBox="0 0 11 14"><path d="M5.5 0C4 4 1 6 1 9a4.5 4.5 0 0 0 9 0c0-3-3-5-4.5-9z" fill="#1f4f60"/></svg>Understand and Communicate<br>Project Cost And Risk</li>
    <li><svg width="11" height="14" viewBox="0 0 11 14"><path d="M5.5 0C4 4 1 6 1 9a4.5 4.5 0 0 0 9 0c0-3-3-5-4.5-9z" fill="#1f4f60"/></svg>Control And Reduce Expenditure</li>
    <li><svg width="11" height="14" viewBox="0 0 11 14"><path d="M5.5 0C4 4 1 6 1 9a4.5 4.5 0 0 0 9 0c0-3-3-5-4.5-9z" fill="#1f4f60"/></svg>Learn And Improve Performance</li>
  </ul>
</div>

<section class="abs services">
  <article class="service s1">
    <div class="service-icon"><svg width="34" height="30" viewBox="0 0 34 30" fill="#fff"><rect x="4" y="14" width="4" height="12"/><rect x="11" y="6" width="4" height="20"/><rect x="18" y="10" width="4" height="16"/><rect x="25" y="2" width="4" height="24"/><rect x="1" y="27" width="32" height="2"/></svg></div>
    <div class="service-body"><h3>Time &amp; Cost Estimation</h3><p>PLX delivers a standardized, systematic approach to understanding project risk.</p><span class="read-more">Read More<b>+</b></span></div>
  </article>
  <article class="service s2">
    <div class="service-icon"><svg width="26" height="34" viewBox="0 0 26 34" fill="#fff"><rect x="0" y="0" width="26" height="34" rx="3"/><rect x="4" y="4" width="18" height="7" fill="#7d8a55"/><g fill="#7d8a55"><rect x="4" y="14" width="4" height="4"/><rect x="11" y="14" width="4" height="4"/><rect x="18" y="14" width="4" height="4"/><rect x="4" y="21" width="4" height="4"/><rect x="11" y="21" width="4" height="4"/><rect x="18" y="21" width="4" height="4"/><rect x="4" y="28" width="4" height="3"/><rect x="11" y="28" width="4" height="3"/><rect x="18" y="28" width="4" height="3"/></g></svg></div>
    <div class="service-body"><h3>Materials &amp; Cost Control</h3><p>CMT has been helping companies optimize materials and cost tracking processes since 1992.</p><span class="read-more">Read More<b>+</b></span></div>
  </article>
  <article class="service s3">
    <div class="service-icon"><svg width="36" height="30" viewBox="0 0 36 30" fill="none" stroke="#fff" stroke-width="2.5"><path d="M2 3h13a3 3 0 0 1 3 3v22a3 3 0 0 0-3-3H2z"/><path d="M34 3H21a3 3 0 0 0-3 3v22a3 3 0 0 1 3-3h13z"/><path d="M6 10h7M6 15h7M6 20h7M23 10h7M23 15h7M23 20h7" stroke-width="2"/></svg></div>
    <div class="service-body"><h3>Lessons Learned</h3><p>LKX is an advanced lessons learned &amp; knowledge system for use in the energy industry.</p><span class="read-more">Read More<b>+</b></span></div>
  </article>
  <article class="service s4">
    <div class="service-icon"><svg width="32" height="32" viewBox="0 0 32 32" fill="#fff"><circle cx="16" cy="10" r="8"/><path d="M2 32c0-9 6-13 14-13s14 4 14 13z"/></svg></div>
    <div class="service-body"><h3>Services &amp; Consulting</h3><p>Successful software implementations rely on people and processes to deliver results.</p><span class="read-more">Read More<b>+</b></span></div>
  </article>
</section>

<section class="abs welcome">
  <h2>Welcome To <strong>Corvani Systems</strong></h2>
  <p>From early phase evaluation through planning, execution and post analysis of wells, we deliver the tools, processes and people required to facilitate major performance improvement and cost savings.</p>
  <p>Our solutions are used in more than 30 countries to support operations ranging from a single well to global deployments with Major Operators.</p>
</section>

<aside class="abs news">
  <div class="news-head">Latest News</div>
  <ul class="news-list">
    <li class="news-item"><div class="news-logo">Corvani</div><div><h4>PLX Offset Data Linker Assisting North Sea Estimates</h4><p>The PLX Offset Data Linker (OFL) is a platform for linking offset data sources...</p></div></li>
    <li class="news-item"><div class="news-logo">Tessaly</div><div><h4>Tessaly implement CMT for UK wells</h4><p>To support materials and cost tracking processes on two wells drilled...</p></div></li>
    <li class="news-item"><div class="news-logo">Solwick</div><div><h4>Solwick Petroleum select CMT</h4><p>CMT has been selected by Solwick Petroleum to support its cost management...</p></div></li>
    <li class="news-item"><div class="news-logo">Arden­moor</div><div><h4>CMT Implementation at Ardenmoor</h4><p>Ardenmoor, the UK focused independent development and production company...</p></div></li>
  </ul>
</aside>

<section class="abs clients">
  <div class="client" style="left:98px">Valmira</div>
  <div class="client" style="left:200px">Norvik</div>
  <div class="client" style="left:302px">Halden</div>
  <div class="client" style="left:404px">KT</div>
  <div class="client" style="left:506px">Ardenmoor</div>
  <div class="client" style="left:608px">Eastfield</div>
  <div class="client" style="left:710px">Marrow</div>
</section>

<footer class="abs site-footer">
  <div class="abs footer-title" style="left:97px;top:18px">Contact Info</div>
  <div class="abs" style="left:97px;top:45px;width:160px">
    <div class="region">EUROPE</div>
    <div class="contact-line"><svg width="9" height="12" viewBox="0 0 9 12"><path d="M4.5 0A4.5 4.5 0 0 0 0 4.5C0 8 4.5 12 4.5 12S9 8 9 4.5A4.5 4.5 0 0 0 4.5 0zm0 6.5a2 2 0 1 1 0-4 2 2 0 0 1 0 4z" fill="#9fc2cc"/></svg>12 Harbour Row Aberdeen<br>AB00 1ZZ</div>
    <div class="contact-line"><svg width="8" height="12" viewBox="0 0 8 12"><rect x=".5" y=".5" width="7" height="11" rx="1.5" fill="none" stroke="#9fc2cc"/><circle cx="4" cy="9.5" r=".8" fill="#9fc2cc"/></svg>Phone :<br>+44(0)1632 960418</div>
    <div class="contact-line"><svg width="11" height="8" viewBox="0 0 11 8"><rect width="11" height="8" fill="#9fc2cc"/><path d="M0 0l5.5 4.5L11 0" fill="none" stroke="#245869"/></svg>Email :<br>eu@corvanisystems.example</div>
  </div>
  <div class="abs" style="left:266px;top:45px;width:170px">
    <div class="region">NORTH AMERICA</div>
    <div class="contact-line"><svg width="9" height="12" viewBox="0 0 9 12"><path d="M4.5 0A4.5 4.5 0 0 0 0 4.5C0 8 4.5 12 4.5 12S9 8 9 4.5A4.5 4.5 0 0 0 4.5 0zm0 6.5a2 2 0 1 1 0-4 2 2 0 0 1 0 4z" fill="#9fc2cc"/></svg>800 Example Parkway Suite 210<br>Houston, TX 77000</div>
    <div class="contact-line"><svg width="8" height="12" viewBox="0 0 8 12"><rect x=".5" y=".5" width="7" height="11" rx="1.5" fill="none" stroke="#9fc2cc"/><circle cx="4" cy="9.5" r=".8" fill="#9fc2cc"/></svg>Phone :<br>(555) 014 2290</div>
    <div class="contact-line"><svg width="11" height="8" viewBox="0 0 11 8"><rect width="11" height="8" fill="#9fc2cc"/><path d="M0 0l5.5 4.5L11 0" fill="none" stroke="#245869"/></svg>Email :<br>us@corvanisystems.example</div>
  </div>
  <div class="abs footer-divider"></div>
  <div class="abs footer-title" style="left:457px;top:18px">Contact Form</div>
  <div class="field" style="left:457px;top:45px;width:165px">First Name</div>
  <div class="field" style="left:629px;top:45px;width:165px">Last Name</div>
  <div class="field" style="left:457px;top:79px;width:165px">Email Address</div>
  <div class="field" style="left:629px;top:79px;width:165px">Company</div>
  <div class="field" style="left:457px;top:112px;width:337px;height:57px">Message</div>
  <div class="abs submit">SUBMIT</div>
</footer>

<div class="abs copyright">© 2013 Corvani Systems Ltd<br>All Rights Reserved</div>
<div class="abs partner-badge" role="img" aria-label="Software partner badge"></div>

</body>
</html>
```